Tolvane Channel Partner Program Brochure

We need a full color brochure designed for our Channel Partner program. The program is intended to recruit agents to sell our services. There's a lot of information to be communicated and the final design should not look too text heavy.

About Tolvane:
Founded in 2007, Tolvane is a global BPO/KPO provider delivering superior managed services in the areas of Managed NOC & Network services, App Development, Service Provisioning, Finance & Accounting, Fraud & Security Management, and IP Support to telecommunications companies worldwide. The company consistently helps its clients to dramatically improve their financial performance through its highly specialized services. Tolvane is headquartered in the Washington, D.C. area. For more information, visit http://www.tolvane-example.com. Follow the company on Twitter @Tolvane.

Target Market(s)

Agents in the U.S. selling telecom products and services.

Industry/Entity Type

Telecommunications

Requirements
Must have
• Brochure is a half fold and the template is attached. Good use of balance between imagery/graphic and text.

```html
<!DOCTYPE html>
<html lang="en">
<head>
<meta charset="utf-8">
<title>Tolvane Channel Partner Program Brochure</title>
<link rel="stylesheet" href="https://fonts.googleapis.com/css2?family=Roboto:wght@300;400;700;900&display=swap">
<style>
  :root{
    --red:#c8171e;
    --red-dark:#8e0f14;
    --red-mid:#b01219;
    --silver-light:#f4f4f4;
    --silver:#d3d4d6;
    --ink:#3a3a3a;
    --ink-soft:#666;
    --paper:#ffffff;
    --stage:#e9e9ea;
  }
  *{box-sizing:border-box;margin:0;padding:0}
  html,body{width:1200px;height:987px;overflow:hidden;background:var(--stage);font-family:"Roboto",Arial,sans-serif;color:var(--ink)}
  .canvas{position:relative;width:1200px;height:987px}
  .spread{position:absolute;left:270px;width:660px;height:460px;display:flex;box-shadow:0 6px 18px rgba(0,0,0,.18)}
  .spread--cover{top:22px}
  .spread--inside{top:505px}
  .page{position:relative;width:330px;height:460px;overflow:hidden}

  /* Cover */
  .back-cover{background:linear-gradient(90deg,var(--red-dark),var(--red) 70%,var(--red-mid))}
  .find-out{position:absolute;left:26px;bottom:40px;font-weight:300;font-size:15px;line-height:16px;color:rgba(255,255,255,.75);letter-spacing:.5px}
  .contact{position:absolute;left:100px;bottom:40px;color:#fff}
  .wordmark{font-weight:900;letter-spacing:.5px}
  .contact .wordmark{font-size:15px;color:#fff;display:block;margin-bottom:4px}
  .contact dl{display:grid;grid-template-columns:34px auto;font-size:6.5px;line-height:9px}
  .contact dt{color:rgba(255,255,255,.8)}
  .front-cover{background:linear-gradient(180deg,var(--red) 0%,var(--red-mid) 100%)}
  .front-band{position:absolute;left:0;top:0;width:330px;height:150px}
  .front-cover .wordmark{position:absolute;left:0;right:0;top:62px;text-align:center;font-size:22px;color:var(--red)}
  .front-title{position:absolute;right:24px;top:240px;text-align:right;color:#fff}
  .front-title h1{font-size:16px;font-weight:900;line-height:17px;text-transform:uppercase}
  .front-title p{margin-top:8px;font-size:11px;font-weight:300;line-height:13px;color:rgba(255,255,255,.8)}

  /* Inside */
  .inside-left,.inside-right{background:var(--paper)}
  .photo{position:absolute}
  .photo--office{left:10px;top:22px;width:150px;height:230px;background:linear-gradient(160deg,#d9dde2,#8a8f96 60%,#3d4046)}
  .photo--kitchen{left:190px;top:300px;width:135px;height:150px;background:linear-gradient(160deg,#e9e3d6,#9c8a74 55%,#4e4a49)}
  .photo--living{left:0;top:22px;width:140px;height:250px;background:linear-gradient(170deg,#f3f3f1,#c9c6c0 55%,#4d5266)}
  .col{position:absolute;font-size:5.6px;line-height:7.6px;color:var(--ink-soft)}
  .col p+p{margin-top:6px}
  .inside-left .wordmark{position:absolute;left:172px;top:26px;font-size:15px;color:var(--red)}
  h2{color:var(--red);font-size:8.5px;font-weight:900;text-transform:uppercase;margin-bottom:4px}
  h3{color:var(--red);font-size:6.5px;font-weight:700;margin-top:7px}
  .overview{left:172px;top:52px;width:148px}
  .who{left:12px;top:300px;width:168px}
  .why{left:150px;top:30px;width:172px}
  .why h2{color:var(--ink);font-size:7.5px}
  .why ul{list-style:none}
  .enroll{left:12px;top:300px;width:306px}
  .enroll ol{padding-left:14px}
  .rule{position:absolute;left:0;right:0;bottom:16px;height:3px;background:var(--red)}
</style>
</head>
<body>
<main class="canvas">

  <section class="spread spread--cover" aria-label="Brochure cover spread">
    <div class="page back-cover">
      <p class="find-out">FIND<br>OUT<br>MORE</p>
      <div class="contact">
        <span class="wordmark">TOLVANE</span>
        <dl>
          <dt>Phone</dt><dd>+1.888.555.0142</dd>
          <dt>Online</dt><dd>www.tolvane-example.com/channel-partners</dd>
          <dt>E-mail</dt><dd>info@tolvane-example.com</dd>
        </dl>
      </div>
    </div>
    <div class="page front-cover">
      <svg class="front-band" viewBox="0 0 330 150" aria-hidden="true">
        <defs>
          <linearGradient id="silver" x1="0" y1="0" x2="1" y2="1">
            <stop offset="0" stop-color="#ffffff"/>
            <stop offset="1" stop-color="#cfd0d2"/>
          </linearGradient>
        </defs>
        <path d="M0 0H330V138Q170 110 0 128Z" fill="url(#silver)"/>
        <path d="M0 128Q170 110 330 138" stroke="#555" stroke-width="1.2" fill="none"/>
      </svg>
      <span class="wordmark">TOLVANE</span>
      <div class="front-title">
        <h1>Tolvane Channel<br>Partner Program</h1>
        <p>A Program designed to make<br>your partnership with Tolvane highly<br>productive and profitable</p>
      </div>
    </div>
  </section>

  <section class="spread spread--inside" aria-label="Brochure inside spread">
    <div class="page inside-left">
      <div class="photo photo--office" role="img" aria-label="Photo of two colleagues working together at an office desk"></div>
      <span class="wordmark">TOLVANE</span>
      <div class="col overview">
        <h2>Overview</h2>
        <p>The Tolvane Partner Program is designed to make your partnership with Tolvane highly productive and profitable. When you offer Tolvane's best-in-class managed services to telco/cable service providers, you'll boost profitability and grow your business.</p>
        <p>Our success is based on yours and we are deeply committed to helping your business prosper.</p>
        <p>Tolvane is a boutique managed services provider offering strategic sourcing solutions to communications companies worldwide. When you transfer your key internal functions to Tolvane, you benefit from improved operational and financial performance, and increase your competitiveness and customer satisfaction through our broad services portfolio. With Tolvane's telco experts managing your key OSS/BSS functions, you are now free to stay focused on sales and marketing activities to drive your company's growth.</p>
      </div>
      <div class="col who">
        <h2>Who is Tolvane?</h2>
        <p>Founded in 2007 and headquartered in the Washington, D.C. area, Tolvane is a global BPO/KPO provider delivering superior managed services in the areas of Managed NOC &amp; Network services, App Development, Service Provisioning, Finance &amp; Accounting, Fraud &amp; Security Management, and IP Support to telecommunications companies worldwide. Tolvane consistently helps its clients to dramatically improve their financial performance through its highly specialized services.</p>
      </div>
      <div class="photo photo--kitchen" role="img" aria-label="Photo of a couple using a laptop at a kitchen counter"></div>
    </div>

    <div class="page inside-right">
      <div class="photo photo--living" role="img" aria-label="Photo of a man relaxing on the floor with a laptop at home"></div>
      <div class="col why">
        <h2>Why become a Tolvane partner?</h2>
        <h3>Growth Opportunities</h3>
        <ul><li>Create competitive differentiation</li><li>Offer greater range of products &amp; services</li><li>Enhance &amp; expand relationship with clients</li><li>Increase revenues, profitability, and success</li></ul>
        <h3>Financial Rewards</h3>
        <ul><li>Aggressive commissions earning potential</li><li>Incentives &amp; promotions</li><li>Earn an additional 5% on your monthly commissions for the first deal</li></ul>
        <h3>Best-in-Class Managed Services</h3>
        <ul><li>NOC &amp; network services</li><li>Service delivery</li><li>Finance &amp; accounting</li><li>Fraud management</li><li>App development</li><li>IP Support</li></ul>
        <h3>Telco Experts</h3>
        <ul><li>Leading global telco-focused MSP</li><li>Decades of experience – telco is in our DNA</li><li>Premier team of certified professionals</li><li>Over 6 years of proven track record delivering operational &amp; financial performance</li></ul>
      </div>
      <div class="col enroll">
        <h2>Enrolling in the Tolvane Channel Partner Program</h2>
        <p>Joining the Tolvane Channel Partner Program is easy.</p>
        <ol>
          <li>Visit www.tolvane-example.com/channel-partners</li>
          <li>Complete our online application form</li>
          <li>Once your application is accepted and you are registered in the program, you will receive a welcome kit and access to sales information</li>
        </ol>
      </div>
      <div class="rule"></div>
    </div>
  </section>

</main>
</body>
</html>
```